3.5" x 11" Door Hanger Design - Residential Roofing Company

We are looking for a double-sided door hanger that we can hang on the doors of prospects. This door hanger would have some brief information about our company, a phone number, website, and then the services that we offer. I don't know that it will have enough room for a lot of pictures, but feel free to use those from the marketing brochure if you think it'll work and I can get you the original as needed.
I have uploaded our certifications, logo, and then our current marketing brochure. The design should be cohesive with our marketing brochure, but doesn't have to match it perfectly.
Lastly, attached is the template that we are planning to print off of. This has a tear off portion at the bottom for a business card for a sales rep. The size of the overall door hanger will be 3.5" x 11", with the bottom 2.5" being the tear off business card with the salesman's information. I'll get you the sales reps information during the final design phase, but we will need name, title, phone number, email, business address, business website, list of services, and then the words "AZ ROC 562071" all on that small portion as well so if they tear it off they still have all the info.

```html
<!DOCTYPE html>
<html lang="en">
<head>
<meta charset="utf-8">
<title>Mesa Ridge Roofing – Door Hangers</title>
<link href="https://fonts.googleapis.com/css2?family=Arvo:wght@700&family=Roboto:wght@400;700&display=swap" rel="stylesheet">
<style>
  :root{
    --backdrop:#3a3a3a;
    --paper:#ffffff;
    --orange:#e65a26;
    --ink:#000000;
    --text:#1a1a1a;
    --badge-green:#2ba24c;
    --badge-navy:#1f3a6e;
    --badge-gold:#c9a84a;
    --photo-tone:#5e6558;
  }
  *{box-sizing:border-box;margin:0;padding:0}
  html,body{width:1200px;height:1200px;overflow:hidden;background:var(--backdrop)}
  .stage{position:relative;width:1200px;height:1200px}
  .hanger{position:absolute;top:62px;width:279px;height:1075px;background:var(--paper);overflow:hidden}
  .hanger--front{left:266px}
  .hanger--back{left:655px}
  .door-hole{position:absolute;left:50%;top:35px;width:138px;height:138px;margin-left:-69px;border-radius:50%;background:var(--ink)}
  .brand{position:absolute;top:260px;left:0;right:0;text-align:center;font-family:'Arvo',serif;font-weight:700;font-size:23px;line-height:30px;color:var(--text)}
  .headline{position:absolute;left:0;right:0;text-align:center;font-family:'Arvo',serif;font-weight:700;font-size:39px;line-height:41px;letter-spacing:.5px;text-transform:uppercase}
  .hanger--front .headline{top:352px;color:var(--orange)}
  .photo{position:absolute;left:0;top:539px;width:279px;height:214px;background:var(--photo-tone)}
  .services{position:absolute;left:0;right:0;text-align:center;font-family:'Roboto',sans-serif;font-size:12px;line-height:14px;letter-spacing:.5px;color:var(--text);text-transform:uppercase}
  .hanger--front .services{top:774px}
  .contact-band{position:absolute;left:0;top:804px;width:279px;height:72px;background:var(--orange)}
  .phone{position:absolute;left:0;right:0;text-align:center;font-family:'Roboto',sans-serif;font-weight:700;font-size:21px;line-height:24px;color:var(--paper)}
  .web{position:absolute;left:0;right:0;text-align:center;font-family:'Roboto',sans-serif;font-size:11px;line-height:13px;color:var(--paper)}
  .hanger--front .phone{top:821px}
  .hanger--front .web{top:849px}
  .tear-off{position:absolute;left:0;top:876px;width:279px;height:199px;background:var(--ink)}
  .headline-panel{position:absolute;left:0;top:338px;width:279px;height:232px;background:var(--ink)}
  .headline-panel__fill{position:absolute;left:22px;right:22px;top:0;bottom:0;background:var(--orange)}
  .hanger--back .headline{top:373px;color:var(--paper)}
  .badge{position:absolute}
  .badge--circle{left:29px;top:598px;width:100px;height:100px;border-radius:50%;background:var(--badge-green)}
  .badge--diamond{left:166px;top:612px;width:70px;height:70px;background:var(--badge-navy);transform:rotate(45deg);border:3px solid var(--badge-gold)}
  .hanger--back .services{top:721px}
  .roof-cta{position:absolute;left:0;top:750px;width:279px;height:126px}
  .hanger--back .phone{top:817px}
  .hanger--back .web{top:845px}
</style>
</head>
<body>
<main class="stage">

  <section class="hanger hanger--front">
    <div class="door-hole"></div>
    <p class="brand">Mesa Ridge Roofing</p>
    <h1 class="headline">Quality<br>Roofing<br>You Can<br>Trust</h1>
    <div class="photo" role="img" aria-label="Photo of a finished home with a new tile roof"></div>
    <p class="services">Tile • Metal • Shingle • Low Slope</p>
    <div class="contact-band"></div>
    <p class="phone">(555) 214-7730</p>
    <p class="web">www.mesaridge-roofing.com</p>
    <div class="tear-off"></div>
  </section>

  <section class="hanger hanger--back">
    <div class="door-hole"></div>
    <p class="brand">Mesa Ridge Roofing</p>
    <div class="headline-panel"><div class="headline-panel__fill"></div></div>
    <h2 class="headline">Quality<br>Roofing<br>You Can<br>Trust</h2>
    <div class="badge badge--circle" role="img" aria-label="Contractor certification badge"></div>
    <div class="badge badge--diamond" role="img" aria-label="Manufacturer certification badge"></div>
    <p class="services">Tile • Metal • Shingle • Low Slope</p>
    <svg class="roof-cta" viewBox="0 0 279 126" aria-hidden="true">
      <polygon points="0,60 139.5,0 279,60 279,126 0,126" fill="#000000"/>
      <polygon points="0,78 139.5,16 279,78 279,126 0,126" fill="#e65a26"/>
    </svg>
    <p class="phone">(555) 214-7730</p>
    <p class="web">www.mesaridge-roofing.com</p>
    <div class="tear-off"></div>
  </section>

</main>
</body>
</html>
```